Morrow Family Reunion Flyer

A flyer detailing family reunion events. It should be complimentary to the logo style and fonts. BE DIFFERENT AVOID TEMPLATES

The 2015 Morrow Family Reunion
Descendants of Tobias Elwin Harold Morrow

Friday August 14th 2pm
Jummah Prayer At Sunvale Mosque
Followed by Family Get Together

Saturday august 15th 12pm
Family Reunion Picnic
4123 morrow Dr.
bowie

Hosted by the Children of The Prestigious Morrow Family

Colors
0355a3
9bcb3c

Requirements
Must have
• Logo

```html
<!DOCTYPE html>
<html lang="en">
<head>
<meta charset="utf-8">
<title>Morrow Family Reunion 2015</title>
<link href="https://fonts.googleapis.com/css2?family=Montserrat:wght@600;700;800&family=Special+Elite&display=swap" rel="stylesheet">
<style>
  :root {
    --paper: #ffffff;
    --earth-dark: #3b332a;
    --earth-mid: #5a5045;
    --earth-light: #6b6256;
    --sand: #d9d2c6;
    --sky-blue: #5b9bd5;
    --family-green: #2e8b3e;
    --ink: #1f1c19;
    --cream: #e8e4dc;
  }
  * { margin: 0; padding: 0; box-sizing: border-box; }
  html, body { width: 854px; height: 1200px; overflow: hidden; background: var(--paper); }
  .flyer {
    position: relative;
    width: 854px; height: 1200px;
    background: var(--paper);
    font-family: "Montserrat", Arial, sans-serif;
  }
  .flyer__sheet {
    position: absolute; left: 15px; top: 18px; width: 823px; height: 1167px;
    background:
      radial-gradient(ellipse at 50% 35%, var(--earth-light) 0%, var(--earth-mid) 45%, var(--earth-dark) 100%);
    overflow: hidden;
  }
  .heading-rule {
    position: absolute; left: 0; width: 823px; height: 3px; background: var(--sky-blue);
  }
  .heading-rule--top { top: 30px; }
  .heading-rule--bottom { top: 73px; }
  .lineage {
    position: absolute; top: 34px; left: 0; width: 823px; height: 38px;
    text-align: center; line-height: 38px;
    color: var(--cream); font-weight: 700; font-size: 27px; letter-spacing: 0.3px;
  }
  .family-mark {
    position: absolute; left: 234px; top: 150px; width: 356px; height: 356px;
    border-radius: 50%; background: var(--sand);
    display: flex; align-items: center; justify-content: center;
  }
  .family-mark__name {
    color: var(--family-green); font-weight: 800; font-size: 34px; text-align: center;
  }
  .title-band {
    position: absolute; left: 0; top: 511px; width: 823px; height: 30px;
    background: var(--sand);
    text-align: center; line-height: 32px;
    font-weight: 700; font-size: 19px; color: var(--family-green);
  }
  .title-band .accent { color: var(--sky-blue); }
  .event { position: absolute; left: 146px; height: 84px; width: 640px; }
  .event--friday { top: 570px; }
  .event--saturday { top: 690px; }
  .event__time {
    position: absolute; left: 0; top: 0; width: 30px; height: 84px;
    display: flex; align-items: center; justify-content: center;
  }
  .event__time span {
    transform: rotate(-90deg); white-space: nowrap;
    color: var(--family-green); font-weight: 700; font-size: 26px;
  }
  .event__date {
    position: absolute; left: 30px; top: 0;
    color: var(--ink); font-weight: 700; line-height: 1;
  }
  .event__day { display: block; font-size: 36px; letter-spacing: -0.5px; }
  .event__day .num { color: var(--sky-blue); }
  .event__month { display: block; font-size: 46px; letter-spacing: -0.5px; margin-top: 2px; }
  .event__details {
    position: absolute; left: 304px; top: 20px;
    color: var(--cream); font-weight: 700; font-size: 12.5px; line-height: 1.45;
  }
  .invite {
    position: absolute; left: 0; width: 823px; text-align: center;
    font-weight: 800; line-height: 1; letter-spacing: 2px;
    paint-order: stroke fill;
  }
  .invite--you {
    top: 825px; font-size: 128px; color: var(--family-green);
    -webkit-text-stroke: 6px #a8a39b;
  }
  .invite--invited {
    top: 935px; font-size: 150px; color: var(--cream);
    -webkit-text-stroke: 8px var(--sky-blue);
  }
  .host-line {
    position: absolute; left: 0; top: 1085px; width: 823px; text-align: center;
    font-family: "Special Elite", "Courier New", monospace;
    text-transform: uppercase; font-size: 23px; color: var(--cream); letter-spacing: 0.5px;
    font-weight: 700;
  }
</style>
</head>
<body>
<main class="flyer">
  <section class="flyer__sheet">
    <div class="heading-rule heading-rule--top"></div>
    <h1 class="lineage">Descendants of Tobias Elwin Harold Morrow</h1>
    <div class="heading-rule heading-rule--bottom"></div>

    <div class="family-mark">
      <span class="family-mark__name">Morrow Family</span>
    </div>

    <h2 class="title-band">Morrow <span class="accent">Family</span> Reunion 2015</h2>

    <article class="event event--friday">
      <div class="event__time"><span>2PM</span></div>
      <div class="event__date">
        <span class="event__day">FRIDAY<span class="num">14</span></span>
        <span class="event__month">AUGUST</span>
      </div>
      <p class="event__details">Jummah Prayer At Sunvale Mosque<br>Followed by Family Get Together</p>
    </article>

    <article class="event event--saturday">
      <div class="event__time"><span>12PM</span></div>
      <div class="event__date">
        <span class="event__day">SATURDAY<span class="num">15</span></span>
        <span class="event__month">AUGUST</span>
      </div>
      <p class="event__details">Family Reunion Picnic<br>4123 Morrow Dr. Bowie</p>
    </article>

    <p class="invite invite--you">YOU ARE</p>
    <p class="invite invite--invited">INVITED!</p>

    <p class="host-line">Hosted by the children of the prestigious Morrow family</p>
  </section>
</main>
</body>
</html>
```